Healthy Snack Bar Wrapper Design

We are passionate about delivering healthy and tasty treats that are Raw, Organic, Preservative Free, Gluten Free, have No Added Sugar and No Additives!
In this project we are looking for a design for a new healthy food product to be launched soon in Australia. The packaging will be a bar wrapper made from foil that will be hot sealed, with a front and a back.
The snack is a raw, organic and healthy treat made predominantly with nuts, and will come in 3 initial flavours:
- Velvet Harbor (Sour Cherry and Choc)
- Plum Fizzaroo (Banana, Apricot and Blueberry)
- Sunmelodia (Pineapple, Passionfruit and Kiwi)
The product name is MunchWell, which does not currently have a logo. We are happy to have this as a simple written component of the initial design at the top of the packaging, perhaps within an circle, square or oval.
The typeface used for the names and the main ingredients should be fun.
The overall design should be very simple and make use of minimal colours. Our preferences are to have a plain colour for the background, such as light organic brown or white, with an eye catching colour that can be used to define the flavour, but should not be too vibrant.
We do not want to have an 3 dimensional images or objects. Nor do we want to have product images and any imagery should be only to give the impression of the flavours within rather than an image of the flavour. Finally, we do not want to have gradients included in the design.
The final design should communicate healthy, tasty and fun!
Examples of inspiration designs are attached in the files.
Main Information:
- The front should comprise of the following information:
-- MunchWell
-- Flavour name (such as Velvet Harbor)
-- Main Ingredients (Sour Cherry and Choc) (This is optional)
-- Portion size (60g)
-- Message (This is optional)
--- 0% Additives
--- 60% Nuts
--- 100% Natural
- The back needs to have space for the following information:
-- Nutritional Information
-- Barcode
-- Ingredients
-- Contact information
- Wrapper Dimensions
-- Width: 14cm
-- Height: 15cm
- Bar Dimensions
-- Width: 3cm
-- Height: 10cm
-- Depth: 2.5cm
Target Market(s)
People who want to have a healthy tasty treat
Colors
Designer to choose colors to be used in the design.
Requirements
Must have
- Main Information:
- - The front should comprise of the following information:
- -- MunchWell
- -- Flavour name (such as Velvet Harbor)
- -- Main Ingredients (Sour Cherry and Choc) (This is optional)
- -- Portion size (60g)
- -- Message (This is optional)
- --- 0% Additives
- --- 60% Nuts
- --- 100% Natural
- - The back needs to have space for the following information:
- -- Nutritional Information
- -- Barcode
- -- Ingredients
- -- Contact information
- - Wrapper Dimensions
- -- Width: 14cm
- -- Height: 15cm
- - Bar Dimensions
- -- Width: 3cm
- -- Height: 10cm
- -- Depth: 2.5cm
Should not have
- We do not want to have an 3 dimensional images or objects. Nor do we want to have product images and any imagery should be only to give the impression of the flavours within rather than an image of the flavour. Finally, we do not want to have gradients included in the design.

```html
<!DOCTYPE html>
<html lang="en">
<head>
<meta charset="utf-8">
<title>MunchWell Snack Bar Wrappers</title>
<link rel="stylesheet" href="https://fonts.googleapis.com/css2?family=Fredoka:wght@500;600;700&display=swap">
<style>
  :root {
    --backdrop: #e4e4e4;
    --kraft: #b59c74;
    --kraft-dark: #a58c64;
    --ink-light: #ffffff;
    --brand-dot: #2b2a6b;
    --cherry: #5e1a40;
    --apricot: #e18b2b;
    --kiwi: #2f9d52;
  }
  * { box-sizing: border-box; margin: 0; padding: 0; }
  html, body { width: 1200px; height: 597px; overflow: hidden; }
  body {
    background: var(--backdrop);
    font-family: "Fredoka", sans-serif;
    position: relative;
  }
  .wrapper {
    position: absolute;
    top: 48px;
    width: 240px;
    height: 500px;
    color: var(--ink-light);
  }
  .wrapper--cherry { left: 130px; --flavour: var(--cherry); }
  .wrapper--apricot { left: 480px; --flavour: var(--apricot); }
  .wrapper--kiwi { left: 830px; --flavour: var(--kiwi); }

  .wrapper__shape { position: absolute; inset: 0; width: 240px; height: 500px; }
  .wrapper__foil { fill: var(--flavour); }
  .wrapper__kraft { fill: var(--kraft); }
  .wrapper__seal { stroke: var(--kraft-dark); stroke-width: 1; fill: none; }
  .wrapper__band { fill: var(--flavour); }

  .brand {
    position: absolute;
    top: 44px; left: 0; right: 0;
    display: flex; align-items: center; justify-content: center; gap: 8px;
    font-weight: 600; font-size: 30px; letter-spacing: 0.5px;
  }
  .brand__dot {
    width: 14px; height: 14px; border-radius: 50%;
    background: var(--brand-dot);
  }
  .flavour {
    position: absolute;
    top: 106px; left: 18px; right: 18px;
    text-align: center;
  }
  .flavour__name { font-weight: 700; font-size: 27px; line-height: 1.05; }
  .flavour__ingredients { font-weight: 500; font-size: 16px; line-height: 1.2; margin-top: 6px; }

  .claims { position: absolute; left: 0; right: 0; top: 300px; }
  .claims__item {
    height: 30px; margin-bottom: 15px;
    display: flex; align-items: center; justify-content: center;
    font-weight: 600; font-size: 17px;
  }
  .portion {
    position: absolute;
    top: 446px; left: 50%; transform: translateX(-50%);
    background: var(--flavour);
    border-radius: 4px;
    padding: 2px 7px;
    font-weight: 600; font-size: 10px;
  }
</style>
</head>
<body>

<!-- Velvet Harbor -->
<div class="wrapper wrapper--cherry">
  <svg class="wrapper__shape" viewBox="0 0 240 500" aria-hidden="true">
    <path class="wrapper__foil" d="M0 10 L5 4 L10 10 L15 4 L20 10 L25 4 L30 10 L35 4 L40 10 L45 4 L50 10 L55 4 L60 10 L65 4 L70 10 L75 4 L80 10 L85 4 L90 10 L95 4 L100 10 L105 4 L110 10 L115 4 L120 10 L125 4 L130 10 L135 4 L140 10 L145 4 L150 10 L155 4 L160 10 L165 4 L170 10 L175 4 L180 10 L185 4 L190 10 L195 4 L200 10 L205 4 L210 10 L215 4 L220 10 L225 4 L230 10 L235 4 L240 10 V240 H0 Z"/>
    <path class="wrapper__kraft" d="M0 222 L20 218 L38 224 L60 214 L82 220 L104 212 L128 219 L150 213 L172 221 L196 215 L218 222 L240 217 V490 L235 496 L230 490 L225 496 L220 490 L215 496 L210 490 L205 496 L200 490 L195 496 L190 490 L185 496 L180 490 L175 496 L170 490 L165 496 L160 490 L155 496 L150 490 L145 496 L140 490 L135 496 L130 490 L125 496 L120 490 L115 496 L110 490 L105 496 L100 490 L95 496 L90 490 L85 496 L80 490 L75 496 L70 490 L65 496 L60 490 L55 496 L50 490 L45 496 L40 490 L35 496 L30 490 L25 496 L20 490 L15 496 L10 490 L5 496 L0 490 Z"/>
    <rect class="wrapper__band" x="0" y="300" width="240" height="30"/>
    <rect class="wrapper__band" x="0" y="345" width="240" height="30"/>
    <rect class="wrapper__band" x="0" y="390" width="240" height="30"/>
    <line class="wrapper__seal" x1="0" y1="472" x2="240" y2="472"/>
  </svg>
  <div class="brand"><span class="brand__name">MunchWell</span><span class="brand__dot"></span></div>
  <div class="flavour">
    <h2 class="flavour__name">VELVET HARBOR</h2>
    <p class="flavour__ingredients">Sour Cherry &amp; Choc</p>
  </div>
  <ul class="claims" style="list-style:none">
    <li class="claims__item">100% Natural</li>
    <li class="claims__item">60% Nuts</li>
    <li class="claims__item">0% Additives</li>
  </ul>
  <span class="portion">60g</span>
</div>

<!-- Plum Fizzaroo -->
<div class="wrapper wrapper--apricot">
  <svg class="wrapper__shape" viewBox="0 0 240 500" aria-hidden="true">
    <path class="wrapper__foil" d="M0 10 L5 4 L10 10 L15 4 L20 10 L25 4 L30 10 L35 4 L40 10 L45 4 L50 10 L55 4 L60 10 L65 4 L70 10 L75 4 L80 10 L85 4 L90 10 L95 4 L100 10 L105 4 L110 10 L115 4 L120 10 L125 4 L130 10 L135 4 L140 10 L145 4 L150 10 L155 4 L160 10 L165 4 L170 10 L175 4 L180 10 L185 4 L190 10 L195 4 L200 10 L205 4 L210 10 L215 4 L220 10 L225 4 L230 10 L235 4 L240 10 V240 H0 Z"/>
    <path class="wrapper__kraft" d="M0 218 L22 224 L44 215 L66 221 L90 213 L112 220 L134 214 L158 222 L180 215 L202 221 L222 214 L240 220 V490 L235 496 L230 490 L225 496 L220 490 L215 496 L210 490 L205 496 L200 490 L195 496 L190 490 L185 496 L180 490 L175 496 L170 490 L165 496 L160 490 L155 496 L150 490 L145 496 L140 490 L135 496 L130 490 L125 496 L120 490 L115 496 L110 490 L105 496 L100 490 L95 496 L90 490 L85 496 L80 490 L75 496 L70 490 L65 496 L60 490 L55 496 L50 490 L45 496 L40 490 L35 496 L30 490 L25 496 L20 490 L15 496 L10 490 L5 496 L0 490 Z"/>
    <rect class="wrapper__band" x="0" y="300" width="240" height="30"/>
    <rect class="wrapper__band" x="0" y="345" width="240" height="30"/>
    <rect class="wrapper__band" x="0" y="390" width="240" height="30"/>
    <line class="wrapper__seal" x1="0" y1="472" x2="240" y2="472"/>
  </svg>
  <div class="brand"><span class="brand__name">MunchWell</span><span class="brand__dot"></span></div>
  <div class="flavour">
    <h2 class="flavour__name">Plum Fizzaroo</h2>
    <p class="flavour__ingredients">Banana, Apricot<br>&amp; Blueberry</p>
  </div>
  <ul class="claims" style="list-style:none">
    <li class="claims__item">100% Natural</li>
    <li class="claims__item">60% Nuts</li>
    <li class="claims__item">0% Additives</li>
  </ul>
  <span class="portion">60g</span>
</div>

<!-- Sunmelodia -->
<div class="wrapper wrapper--kiwi">
  <svg class="wrapper__shape" viewBox="0 0 240 500" aria-hidden="true">
    <path class="wrapper__foil" d="M0 10 L5 4 L10 10 L15 4 L20 10 L25 4 L30 10 L35 4 L40 10 L45 4 L50 10 L55 4 L60 10 L65 4 L70 10 L75 4 L80 10 L85 4 L90 10 L95 4 L100 10 L105 4 L110 10 L115 4 L120 10 L125 4 L130 10 L135 4 L140 10 L145 4 L150 10 L155 4 L160 10 L165 4 L170 10 L175 4 L180 10 L185 4 L190 10 L195 4 L200 10 L205 4 L210 10 L215 4 L220 10 L225 4 L230 10 L235 4 L240 10 V240 H0 Z"/>
    <path class="wrapper__kraft" d="M0 221 L18 215 L40 222 L62 216 L86 223 L108 214 L130 220 L152 213 L176 219 L198 214 L220 221 L240 216 V490 L235 496 L230 490 L225 496 L220 490 L215 496 L210 490 L205 496 L200 490 L195 496 L190 490 L185 496 L180 490 L175 496 L170 490 L165 496 L160 490 L155 496 L150 490 L145 496 L140 490 L135 496 L130 490 L125 496 L120 490 L115 496 L110 490 L105 496 L100 490 L95 496 L90 490 L85 496 L80 490 L75 496 L70 490 L65 496 L60 490 L55 496 L50 490 L45 496 L40 490 L35 496 L30 490 L25 496 L20 490 L15 496 L10 490 L5 496 L0 490 Z"/>
    <rect class="wrapper__band" x="0" y="300" width="240" height="30"/>
    <rect class="wrapper__band" x="0" y="345" width="240" height="30"/>
    <rect class="wrapper__band" x="0" y="390" width="240" height="30"/>
    <line class="wrapper__seal" x1="0" y1="472" x2="240" y2="472"/>
  </svg>
  <div class="brand"><span class="brand__name">MunchWell</span><span class="brand__dot"></span></div>
  <div class="flavour">
    <h2 class="flavour__name">Sunmelodia</h2>
    <p class="flavour__ingredients">Pineapple,<br>Passionfruit &amp; Kiwi</p>
  </div>
  <ul class="claims" style="list-style:none">
    <li class="claims__item">100% Natural</li>
    <li class="claims__item">60% Nuts</li>
    <li class="claims__item">0% Additives</li>
  </ul>
  <span class="portion">60g</span>
</div>

</body>
</html>
```